Business Card Design

We would like to re-design our business cards. Our Company - Quarvel Turbochargers, rebuilds turbochargers and sells replacement parts. Our website is: http://www.quarvelturbochargers.example
We just had our logo changed. I will attach the file. Looking for fresh new/modern business card. We like the colors red, black, white and silver. Black background looks attractive, but not a requirement. The final design should communicate reasonable/competitive prices, top quality and reliability of our products.
Updates
Project Deadline Extended
Reason: Need to finalize the info on the card. Currently working on changing address and email info. Want to make sure it is the correct one before accepting the final design. Unless, this is something that can be changed at a later time..??
Industry/Entity Type
Business
Contact Information for Business Card
QUARVEL TURBOCHARGERS, LLC
20473 Harrow Bend SE
Massillon, OH 44902
Tel: +1-330-555-0142
Fax: +1-330-555-0187
info@QuarvelTurbochargers.example
Our current business card had the following highlights:
*We rebuild all Turbocharges for Automotive, Diesel and Industrial
*Precision Balancing and in-house turbocharger needs
*All Turbocharger replacement parts are made in USA / U.K.
Look and feel
Each slider illustrates characteristics of the customer's brand and the style your logo design should communicate.

```html
<!DOCTYPE html>
<html lang="en">
<head>
<meta charset="utf-8">
<title>Quarvel Turbochargers – Business Card</title>
<link href="https://fonts.googleapis.com/css2?family=Arimo:wght@400;700&display=swap" rel="stylesheet">
<style>
  :root {
    --red: #e0232e;
    --black: #1c1c1e;
    --black-deep: #111113;
    --white: #f4f4f4;
    --silver: #c9c9c9;
    --text-light: #e6e6e6;
    --stage: #d9d9d9;
  }
  * { box-sizing: border-box; margin: 0; padding: 0; }
  html, body {
    width: 1200px; height: 780px; overflow: hidden;
    background: var(--stage);
    font-family: "Arimo", Arial, sans-serif;
  }
  .stage {
    width: 1200px; height: 780px;
    display: flex; align-items: center; justify-content: center; gap: 40px;
  }
  .card {
    width: 540px; height: 309px; position: relative; overflow: hidden;
    box-shadow: 0 6px 18px rgba(0,0,0,.25);
  }

  /* Front */
  .card-front { background: var(--white); }
  .front-brand {
    height: 132px; display: flex; align-items: center; justify-content: center; gap: 14px;
    background: linear-gradient(180deg, #ffffff, #ececec);
  }
  .brand-dot { width: 26px; height: 26px; border-radius: 50%; background: var(--red); }
  .brand-name {
    font-weight: 700; font-size: 30px; color: var(--black); letter-spacing: .5px;
  }
  .front-band { height: 16px; background: var(--red); }
  .front-info {
    position: absolute; left: 0; right: 0; top: 148px; bottom: 0;
    background: linear-gradient(180deg, #222225, var(--black-deep));
    padding: 22px 34px;
  }
  .person {
    color: var(--red); font-size: 19px; display: flex; align-items: center; gap: 10px;
  }
  .person-name { font-weight: 400; letter-spacing: .3px; }
  .person-sep { width: 1px; height: 18px; background: var(--text-light); opacity: .6; }
  .person-title { font-size: 14px; }
  .contacts {
    margin-top: 34px; display: flex; align-items: center; gap: 26px;
    color: var(--text-light); font-size: 13px; line-height: 1.45;
  }
  .contact-divider { width: 1px; height: 44px; background: var(--red); }
  .contact-line { display: flex; align-items: center; gap: 8px; }
  .icon { width: 12px; height: 12px; flex: none; }

  /* Back */
  .card-back { background: linear-gradient(180deg, #232326, var(--black-deep)); }
  .back-band {
    position: absolute; left: 0; right: 0; top: 84px; height: 141px;
    display: flex; flex-direction: column;
  }
  .back-rule { height: 3px; background: var(--red); }
  .back-gap { height: 6px; }
  .back-panel {
    flex: 1; background: linear-gradient(180deg, #ffffff, #e9e9e9);
    display: flex; align-items: center; justify-content: center; gap: 14px;
  }
</style>
</head>
<body>
<main class="stage">
  <section class="card card-front" aria-label="Business card front">
    <div class="front-brand">
      <span class="brand-dot"></span>
      <span class="brand-name">Quarvel Turbochargers</span>
    </div>
    <div class="front-band"></div>
    <div class="front-info">
      <div class="person">
        <span class="person-name">EMPLOYEE NAME</span>
        <span class="person-sep"></span>
        <span class="person-title">Managing Director</span>
      </div>
      <div class="contacts">
        <address class="contact-address" style="font-style:normal">
          20473 Harrow Bend SE<br>Massillon Ohio 44902
        </address>
        <span class="contact-divider"></span>
        <div class="contact-list">
          <div class="contact-line">
            <svg class="icon" viewBox="0 0 12 12"><rect width="12" height="12" rx="2" fill="#e0232e"/><path d="M3.5 3 L5 3 L5.6 4.6 L4.8 5.3 Q5.6 6.8 6.8 7.2 L7.5 6.4 L9 7 L9 8.5 Q5.5 9 3.5 3Z" fill="#fff"/></svg>
            <span>330-555-0142</span>
          </div>
          <div class="contact-line">
            <svg class="icon" viewBox="0 0 12 12"><rect width="12" height="12" rx="2" fill="#e0232e"/><circle cx="6" cy="6" r="3.2" fill="none" stroke="#fff" stroke-width="1"/><path d="M2.8 6 H9.2 M6 2.8 V9.2" stroke="#fff" stroke-width=".8"/></svg>
            <span>www.quarvelturbochargers.example</span>
          </div>
        </div>
      </div>
    </div>
  </section>

  <section class="card card-back" aria-label="Business card back">
    <div class="back-band">
      <div class="back-rule"></div>
      <div class="back-gap"></div>
      <div class="back-panel">
        <span class="brand-dot"></span>
        <span class="brand-name">Quarvel Turbochargers</span>
      </div>
      <div class="back-gap"></div>
      <div class="back-rule"></div>
    </div>
  </section>
</main>
</body>
</html>
```